Exercise Physiologist needs business cards

I have a logo, I need business cards (Sole trader) as I am moving to a new location and would like an updated look. I provide gym based exercise rehabilitation, injury prevention and movement assessments. I have over 13 years experience as an Exercise Physiologist. I would like the cards to look professional but not boring and can be a little different to stand out when sitting with other Allied Health Professional cards.

Target Market(s)

GP's, Allied health practitioners, people with injuries wanting to exercise

Industry/Entity Type

Health And Wellness

Contact Information for Business Card

Megan Dorrit - Exercise Physiologist 0437 582 906
14 Larkspur Bend Rd
Calder Point
(Gate 5, Brannock Fitness)
vantorahealth@maildrop-example.com
socialpage-example.com/Vantora

Requirements
Must have
• I would like to include a section to add next appointment date and time space to the back of the card.
Nice to have
• Rounded corners and a black background on 1 or 2 sides.
Should not have
• Pictures of fit/toned bodies etc

```html
<!DOCTYPE html>
<html lang="en">
<head>
<meta charset="utf-8">
<title>Vantora Health – Business Cards</title>
<link rel="stylesheet" href="https://fonts.googleapis.com/css2?family=Montserrat:wght@300;400;600;700&display=swap">
<style>
  :root {
    --backdrop: #b8c8d0;
    --card-white: #fbfbfb;
    --brand-navy: #1f4fb0;
    --brand-blue: #55a6d8;
    --ink: #3a3f47;
    --faint-fill: #e4edf4;
    --rule: #8a8f96;
  }
  * { margin: 0; padding: 0; box-sizing: border-box; }
  html, body {
    width: 1200px; height: 800px; overflow: hidden;
    background: var(--backdrop);
    font-family: "Montserrat", sans-serif;
  }
  .sheet {
    position: relative; width: 1200px; height: 800px;
    display: flex; align-items: center; justify-content: center; gap: 48px;
  }
  .card {
    position: relative; width: 520px; height: 297px;
    overflow: hidden; border-radius: 4px;
    box-shadow: 0 10px 24px rgba(40, 60, 80, 0.18);
  }

  /* Front */
  .card--front { background: var(--card-white); }
  .front__decor {
    position: absolute; right: -46px; top: -70px;
    width: 210px; height: 210px; border-radius: 50%;
    background: var(--faint-fill);
  }
  .brand {
    position: absolute; left: 40px; top: 92px;
    display: flex; align-items: center; gap: 12px;
  }
  .brand__dot {
    width: 58px; height: 58px; border-radius: 50%;
    background: var(--brand-blue);
  }
  .brand__name {
    font-size: 40px; font-weight: 400; color: var(--brand-navy);
    letter-spacing: 0.5px;
  }
  .person { position: absolute; left: 170px; top: 166px; }
  .person__name { font-size: 21px; color: var(--brand-navy); line-height: 1; }
  .person__name b { font-weight: 700; }
  .person__name span { font-weight: 300; }
  .person__role { font-size: 11px; color: var(--ink); margin-top: 4px; font-weight: 400; }
  .contact {
    position: absolute; left: 130px; top: 218px;
    list-style: none; font-size: 11.5px; color: var(--ink); font-weight: 400;
  }
  .contact__item { display: flex; align-items: flex-start; gap: 12px; margin-bottom: 6px; line-height: 1.35; }
  .contact__icon {
    flex: none; width: 16px; height: 16px; border-radius: 50%;
    background: var(--brand-blue); display: flex; align-items: center; justify-content: center;
  }

  /* Back */
  .card--back { background: var(--brand-blue); }
  .back__mark {
    position: absolute; left: 56px; top: 70px;
    width: 170px; height: 170px; border-radius: 50%;
    background: var(--card-white);
    display: flex; align-items: center; justify-content: center;
  }
  .back__name { font-size: 22px; font-weight: 400; color: var(--brand-navy); }
  .appointment { position: absolute; right: 42px; top: 70px; width: 228px; }
  .appointment__title {
    font-size: 10.5px; font-weight: 700; letter-spacing: 1px;
    color: var(--brand-navy); text-transform: uppercase; margin-bottom: 4px;
  }
  .appointment__box {
    background: var(--card-white); border: 1px solid var(--brand-navy);
    padding: 14px 14px 10px;
  }
  .appointment__line {
    display: flex; align-items: flex-end; gap: 6px;
    font-size: 10.5px; color: var(--ink); margin-bottom: 10px;
  }
  .appointment__line::after {
    content: ""; flex: 1; border-bottom: 1px dotted var(--rule); margin-bottom: 3px;
  }
</style>
</head>
<body>
<main class="sheet">
  <section class="card card--front" aria-label="Business card front">
    <div class="front__decor" aria-hidden="true"></div>
    <div class="brand">
      <span class="brand__dot" aria-hidden="true"></span>
      <span class="brand__name">Vantora</span>
    </div>
    <div class="person">
      <p class="person__name"><b>Megan</b> <span>Dorrit</span></p>
      <p class="person__role">Exercise Physiologist</p>
    </div>
    <ul class="contact">
      <li class="contact__item">
        <span class="contact__icon">
          <svg width="9" height="9" viewBox="0 0 24 24" aria-hidden="true"><path fill="#fff" d="M6.6 10.8a15 15 0 0 0 6.6 6.6l2.2-2.2c.3-.3.7-.4 1-.2 1.1.4 2.3.6 3.6.6.6 0 1 .4 1 1V20c0 .6-.4 1-1 1A17 17 0 0 1 3 4c0-.6.4-1 1-1h3.5c.6 0 1 .4 1 1 0 1.3.2 2.5.6 3.6.1.3 0 .7-.2 1z"/></svg>
        </span>
        <span>0437 582 906</span>
      </li>
      <li class="contact__item">
        <span class="contact__icon">
          <svg width="9" height="9" viewBox="0 0 24 24" aria-hidden="true"><path fill="#fff" d="M12 2a7 7 0 0 0-7 7c0 5.3 7 13 7 13s7-7.7 7-13a7 7 0 0 0-7-7zm0 9.5A2.5 2.5 0 1 1 12 6.5a2.5 2.5 0 0 1 0 5z"/></svg>
        </span>
        <span>14 Larkspur Bend Rd, Calder Point<br>(Gate 5, Brannock Fitness)</span>
      </li>
    </ul>
  </section>

  <section class="card card--back" aria-label="Business card back">
    <div class="back__mark"><span class="back__name">Vantora</span></div>
    <div class="appointment">
      <p class="appointment__title">Next Appointment</p>
      <div class="appointment__box">
        <p class="appointment__line">Date:</p>
        <p class="appointment__line">Time:</p>
      </div>
    </div>
  </section>
</main>
</body>
</html>
```